Catering Company Needs a Web Page Design

I already have my logo, and so I'm moving onto the next phase.. the web page design. Zestora is a gourmet catering company based in orlando, fl, set to launch in 2015. I will have a store location to host cooking classes as well.... and will be uploading cooking demo videos to my website weekly. Id like a blog section, and about, a video section, contact form, Services, Menu Samples..... My logo and concept is modern, innovative, and fun! I am targeting middle class to upper middle class women, but i want the site to be super unique.

Industry/Entity Type

Catering

Requirements
Must have
• The front/main page must have the logo... and the quillnote registry's definition of "zestora". I like movement... maybe the top banner can move somehow.. Im not a web designer, so i wont really know until I start seeing some examples. For now I dont have photos of my own cooking, so if you could use stock photos of catering dishes.. I uploaded a transparent logo also, maybe that could be the top banner placed over a scene of expertly plated hordourves...

```html
<!DOCTYPE html>
<html lang="en">
<head>
<meta charset="utf-8">
<title>Zestora — Gourmet Catering</title>
<link href="https://fonts.googleapis.com/css2?family=Open+Sans:wght@400;600;700&display=swap" rel="stylesheet">
<style>
:root{
  --green:#6f9a1e;
  --green-dark:#4f7412;
  --orange:#f0a11c;
  --orange-dark:#d88a0c;
  --ink:#333333;
  --muted:#777777;
  --line:#e2e2e2;
  --panel:#f6f6f6;
  --page:#ffffff;
  --footer:#efefef;
  --link:#2f7fc1;
}
*{box-sizing:border-box;margin:0;padding:0}
html,body{width:1200px;height:2588px;overflow:hidden}
body{background:var(--page);font-family:"Open Sans",Arial,sans-serif;color:var(--ink);position:relative}
.abs{position:absolute}

/* header */
.site-header{left:0;top:0;width:1200px;height:88px;background:#fff;border-bottom:1px solid var(--line)}
.brand{left:128px;top:14px}
.brand-name{font-size:44px;font-weight:700;color:var(--ink);letter-spacing:-1px;line-height:46px}
.brand-tag{font-size:10px;color:var(--muted);margin-top:2px}
.main-nav{left:430px;top:0;height:88px;display:flex}
.main-nav a{display:block;padding:0 18px;line-height:70px;font-size:16px;font-weight:600;color:var(--ink);text-decoration:none;border-bottom:3px solid transparent;height:70px}
.main-nav a.active{color:var(--green);border-bottom-color:var(--green)}

/* hero */
.hero{left:0;top:88px;width:1200px;height:392px;background:linear-gradient(120deg,#dcd6c8 0%,#c99a6d 38%,#d8743f 60%,#9bb35a 82%,#efe3b5 100%)}
.hero-def{left:128px;top:232px;width:328px;padding:18px 20px;background:rgba(40,40,40,.72);color:#fff}
.hero-def h2{font-size:20px;font-weight:700}
.hero-def h2 span{font-weight:400;font-size:16px;opacity:.85}
.hero-def p{font-size:15px;line-height:21px;margin-top:6px}
.hero-dots{left:564px;top:454px;display:flex;gap:10px}
.hero-dots i{display:block;width:12px;height:12px;border-radius:50%;background:rgba(255,255,255,.6)}
.hero-dots i.on{background:#fff}

/* blog */
.section-title{font-size:18px;font-weight:700;color:var(--orange)}
.post{left:128px;width:624px}
.post-media{width:624px;height:224px}
.post-title{font-size:14px;font-weight:700;line-height:20px;margin-top:12px}
.post-body{font-size:13px;line-height:19px;color:var(--muted);margin-top:6px}
.post-foot{display:flex;justify-content:space-between;align-items:center;margin-top:12px}
.share{display:flex;gap:6px}
.share span{font-size:11px;border:1px solid #ccc;border-radius:3px;padding:2px 8px;color:#555;background:#f7f7f7}
.read-more{background:var(--orange);color:#fff;font-size:13px;font-weight:700;padding:8px 16px;border-radius:3px}

.pager{left:128px;top:2404px;display:flex;gap:8px}
.pager span{display:block;min-width:30px;height:30px;line-height:28px;text-align:center;font-size:12px;border:1px solid #ccc;color:#666;padding:0 6px}
.pager span.on{background:#444;color:#fff;border-color:#444}

/* sidebar */
.search{left:772px;top:544px;width:300px;height:58px;background:var(--orange);padding:14px 12px;display:flex;gap:6px}
.search .field{flex:1;background:#fff;border:2px solid var(--orange-dark);height:30px;font-size:11px;color:#aaa;padding:6px 8px}
.search .go{background:var(--green);color:#fff;font-size:11px;font-weight:700;padding:0 14px;line-height:30px}
.widget{left:772px;width:300px;background:var(--panel);border:1px solid var(--line);padding:18px 20px}
.widget h3{font-size:16px;font-weight:600;color:var(--muted);margin-bottom:14px}
.recent p{font-size:13px;line-height:19px;color:var(--muted);padding-bottom:14px;margin-bottom:14px;border-bottom:1px solid var(--line)}
.recent p:last-child{border:none;margin:0}
.feeds h3{color:var(--orange);display:flex;justify-content:space-between}
.tweet{display:flex;gap:10px;margin-bottom:18px}
.tweet .av{width:28px;height:28px;background:var(--green);flex:none;border-radius:3px}
.tweet p{font-size:13px;line-height:19px;color:#555}
.tweet a{color:var(--link);text-decoration:none}
.tweet .acts{font-size:11px;color:#888;margin-top:6px;display:flex;gap:14px}
.social-box{left:772px;top:1472px;width:300px;height:288px;border:1px solid #bbb;background:#fff}
.social-box .bar{background:#f2f2f2;border-bottom:1px solid #ccc;font-size:12px;font-weight:700;padding:8px 10px;color:#444}
.social-box .name{font-size:34px;font-weight:700;color:var(--ink);padding:12px 14px 4px}
.social-box .btn{margin:4px 14px;display:inline-block;font-size:11px;border:1px solid #ccc;padding:2px 10px;background:#f6f6f6}
.social-box .count{font-size:11px;color:#666;padding:6px 14px}
.fans{display:flex;gap:8px;padding:0 14px}
.fans div{text-align:center;font-size:10px;color:#666}
.fans i{display:block;width:40px;height:40px;background:#cfcfcf;margin-bottom:3px}
.tags-title{left:772px;top:1792px;font-size:16px;font-weight:600;color:var(--muted)}
.tags{left:772px;top:1826px;width:300px;display:flex;flex-wrap:wrap;gap:10px}
.tags span{background:var(--orange);color:#fff;font-size:11px;padding:4px 12px 4px 10px;border-radius:2px}

/* footer */
.site-footer{left:0;top:2492px;width:1200px;height:96px;background:var(--footer);border-top:1px solid var(--line)}
.foot-nav{left:128px;top:2516px;font-size:13px;color:#555;display:flex;gap:14px}
.copy{left:128px;top:2546px;font-size:12px;color:#888}
.foot-social{left:976px;top:2512px;display:flex;gap:12px}
.foot-social svg{display:block}
</style>
</head>
<body>

<header class="site-header abs">
  <div class="brand abs">
    <div class="brand-name">zestora</div>
    <div class="brand-tag">gourmet catering &amp; cooking classes</div>
  </div>
  <nav class="main-nav abs">
    <a class="active">Home</a><a>About Us</a><a>Services</a><a>Videos</a><a>Blog</a><a>Contact Us</a>
  </nav>
</header>

<section class="hero abs" role="img" aria-label="Banner photo of plated grilled salmon with asparagus and lemon"></section>
<div class="hero-def abs">
  <h2>zestora <span>(zes-tor-ah) noun</span></h2>
  <p>Those who are overly zealous and enthusiastic about cooking, eating, and fine dining</p>
</div>
<div class="hero-dots abs"><i class="on"></i><i></i><i></i><i></i></div>

<h2 class="section-title abs" style="left:128px;top:520px">Blog Posts</h2>

<article class="post abs" style="top:560px">
  <div class="post-media" role="img" aria-label="Photo of grilled fish fillet with asparagus" style="background:linear-gradient(135deg,#e8e2d6,#c98a4e 50%,#6f8a3a)"></div>
  <h3 class="post-title">Sed ut perspiciatis unde omnis iste natus error sit voluptatem accusantium doloremque laudantium, totam rem aperiam</h3>
  <p class="post-body">Nemo enim ipsam voluptatem quia voluptas sit aspernatur aut odit aut fugit, sed quia consequuntur magni dolores eos qui ratione voluptatem sequi nesciunt. Neque porro quisquam est, qui dolorem ipsum quia dolor sit amet, consectetur, adipisci velit, sed quia non numquam eius modi tempora incidunt ut labore et dolore magnam.</p>
  <div class="post-foot"><div class="share"><span>Like</span><span>Share</span><span>Save</span></div><span class="read-more">Read More</span></div>
</article>

<article class="post abs" style="top:1018px">
  <div class="post-media" role="img" aria-label="Photo of a plated dessert with berries" style="background:linear-gradient(135deg,#3a1a12,#b0301e 45%,#e6b46a 80%,#5a3a20)"></div>
  <h3 class="post-title">Sed ut perspiciatis unde omnis iste natus error sit voluptatem accusantium doloremque laudantium, totam rem aperiam</h3>
  <p class="post-body">Nemo enim ipsam voluptatem quia voluptas sit aspernatur aut odit aut fugit, sed quia consequuntur magni dolores eos qui ratione voluptatem sequi nesciunt. Neque porro quisquam est, qui dolorem ipsum quia dolor sit amet, consectetur, adipisci velit, sed quia non numquam eius modi tempora incidunt ut labore et dolore magnam.</p>
  <div class="post-foot"><div class="share"><span>Like</span><span>Share</span><span>Save</span></div><span class="read-more">Read More</span></div>
</article>

<article class="post abs" style="top:1476px">
  <div class="post-media" role="img" aria-label="Photo of gourmet burgers with fries" style="background:linear-gradient(135deg,#f2efe8,#c98b3a 45%,#8a4a22 70%,#e8d8b0)"></div>
  <h3 class="post-title">Sed ut perspiciatis unde omnis iste natus error sit voluptatem accusantium doloremque laudantium, totam rem aperiam</h3>
  <p class="post-body">Nemo enim ipsam voluptatem quia voluptas sit aspernatur aut odit aut fugit, sed quia consequuntur magni dolores eos qui ratione voluptatem sequi nesciunt. Neque porro quisquam est, qui dolorem ipsum quia dolor sit amet, consectetur, adipisci velit, sed quia non numquam eius modi tempora incidunt ut labore et dolore magnam.</p>
  <div class="post-foot"><div class="share"><span>Like</span><span>Share</span><span>Save</span></div><span class="read-more">Read More</span></div>
</article>

<article class="post abs" style="top:1934px">
  <div class="post-media" role="img" aria-label="Photo of a grilled chicken salad plate" style="background:linear-gradient(135deg,#f4f2ee,#d9b47a 45%,#7a9a3e 75%,#eeeae2)"></div>
  <h3 class="post-title">Sed ut perspiciatis unde omnis iste natus error sit voluptatem accusantium doloremque laudantium, totam rem aperiam</h3>
  <p class="post-body">Nemo enim ipsam voluptatem quia voluptas sit aspernatur aut odit aut fugit, sed quia consequuntur magni dolores eos qui ratione voluptatem sequi nesciunt. Neque porro quisquam est, qui dolorem ipsum quia dolor sit amet, consectetur, adipisci velit, sed quia non numquam eius modi tempora incidunt ut labore et dolore magnam.</p>
  <div class="post-foot"><div class="share"><span>Like</span><span>Share</span><span>Save</span></div><span class="read-more">Read More</span></div>
</article>

<nav class="pager abs"><span>‹</span><span>1</span><span>2</span><span>3</span><span class="on">4</span><span>5</span><span>…</span><span>19</span><span>20</span><span>›</span></nav>

<aside>
  <div class="search abs"><div class="field">Search...</div><div class="go">Search</div></div>

  <div class="widget recent abs" style="top:620px;height:400px">
    <h3>Recent Posts</h3>
    <p>At vero eos et accusamus et iusto odio dignissimos ducimus qui</p>
    <p>Blanditiis praesentium voluptatum deleniti atque corrupti quos dolores</p>
    <p>Et harum quidem rerum facilis est et expedita distinctio nam libero</p>
    <p>Temporibus autem quibusdam et aut officiis debitis aut rerum</p>
  </div>

  <div class="widget feeds abs" style="top:1060px;height:380px">
    <h3>Warblenote Feeds <span>→</span></h3>
    <div class="tweet"><div class="av"></div><div><p>Online and high-tech start-ups could account for 4% <a>zsto.ra/4kq2</a></p><div class="acts"><span>Reply</span><span>Repost</span><span>Favourite</span></div></div></div>
    <div class="tweet"><div class="av"></div><div><p>Online and high-tech start-ups could account for 4% <a>zsto.ra/7mb9</a></p><div class="acts"><span>Reply</span><span>Repost</span><span>Favourite</span></div></div></div>
  </div>

  <div class="social-box abs">
    <div class="bar">Find us on Huddlenook</div>
    <div class="name">zestora</div>
    <span class="btn">Like</span>
    <div class="count">1,245 people like Zestora</div>
    <div class="fans">
      <div><i></i>Ana</div><div><i></i>Mia</div><div><i></i>Leo</div><div><i></i>Ivy</div><div><i></i>Sam</div>
    </div>
    <div class="count">Huddlenook social plugin</div>
  </div>

  <h3 class="tags-title abs">Tags</h3>
  <div class="tags abs">
    <span>catering</span><span>recipes</span><span>classes</span><span>gourmet</span><span>dinner</span><span>brunch</span><span>events</span><span>desserts</span><span>videos</span><span>menus</span><span>seafood</span><span>salads</span><span>orlando</span><span>chef</span>
  </div>
</aside>

<footer class="site-footer abs"></footer>
<nav class="foot-nav abs"><span>Home</span><span>|</span><span>About Us</span><span>|</span><span>Services</span><span>|</span><span>Videos</span><span>|</span><span>Blog</span><span>|</span><span>Contact Us</span></nav>
<p class="copy abs">© 2014 Zestora. All Rights Reserved</p>
<div class="foot-social abs">
  <svg width="40" height="40" viewBox="0 0 40 40" aria-hidden="true"><circle cx="20" cy="20" r="20" fill="#555"/></svg>
  <svg width="40" height="40" viewBox="0 0 40 40" aria-hidden="true"><circle cx="20" cy="20" r="20" fill="#555"/></svg>
</div>

</body>
</html>
```